Design Cloud for Core Values & Attributes

See Image Example Below "Word Cloud" this is what we would like this to look like.
The second image is all of the Core Value and Attributes I will list below.
CORE VALUES need to be the bigger words (based off the image I sent) Capitalized, BOLD, Navy
Independence, Capitalism, Trust, Fun, Safety, Growth
ATTRIBUTES need to be the smaller words, lower case, non-bold, lighter blue mixed in (based off the image I sent):
Humility, Consistency, Open Mindedness, Curiosity, Selflessness, Caring, Conscientiousness, Honorable, Cunning, Competitive, Compartmentalization, Innovative, Perseverance, Authenticity, Decisiveness, Self-efficacy, Accountability, Generosity, Humor, Optimism, Resilience, Inclusive, Insouciance to what others think, Courage, Decisive, Curious, Integrity

```html
<!DOCTYPE html>
<html lang="en">
<head>
<meta charset="utf-8">
<title>Core Values</title>
<link rel="stylesheet" href="https://fonts.googleapis.com/css2?family=Archivo:wght@800&family=Bebas+Neue&family=Montserrat:wght@400&display=swap">
<style>
  :root {
    --navy: #160766;
    --rule-blue: #2a2d8f;
    --teal: #5e9693;
    --ink: #222222;
    --card: #ffffff;
    --backdrop: #e2e2e2;
  }
  html, body {
    margin: 0;
    padding: 0;
    width: 1200px;
    height: 1200px;
    overflow: hidden;
    background: var(--backdrop);
  }
  .poster {
    position: absolute;
    left: 0;
    top: 137px;
    width: 1200px;
    height: 925px;
    display: block;
  }
  .poster-ground { fill: var(--card); }
  .headline {
    font-family: "Bebas Neue", "Oswald", sans-serif;
    fill: var(--navy);
  }
  .value {
    font-family: "Archivo", "Arial Black", sans-serif;
    font-weight: 800;
    fill: var(--teal);
  }
  .attributes {
    font-family: "Montserrat", "Helvetica Neue", sans-serif;
    font-weight: 400;
    font-size: 25px;
    letter-spacing: 0.5px;
    fill: var(--ink);
  }
  .attributes-right { text-anchor: end; }
  .rule-navy { fill: var(--rule-blue); }
  .rule-teal { fill: var(--teal); }
  .block-teal { fill: var(--teal); }
  .footer-band { fill: var(--navy); }
</style>
</head>
<body>
<svg class="poster" viewBox="0 0 1686 1300" preserveAspectRatio="none" role="img" aria-label="Core values word layout">
  <rect class="poster-ground" x="0" y="0" width="1686" height="1300"/>

  <!-- top rule -->
  <rect class="rule-navy" x="218" y="123" width="430" height="6"/>

  <!-- FUN -->
  <text class="value" font-size="90" textLength="175" lengthAdjust="spacingAndGlyphs" transform="translate(286 369) rotate(-90)">FUN</text>
  <text class="attributes" x="325">
    <tspan x="325" y="212">Humor Optimism</tspan>
    <tspan x="325" y="243">Humility Resilience</tspan>
    <tspan x="325" y="274">Inclusive</tspan>
    <tspan x="325" y="305">Insouciance to what</tspan>
    <tspan x="325" y="336">others think</tspan>
    <tspan x="325" y="367">Caring</tspan>
  </text>

  <!-- SAFETY -->
  <text class="value" font-size="92" textLength="350" lengthAdjust="spacingAndGlyphs" transform="translate(758 459) rotate(-90)">SAFETY</text>
  <text class="attributes">
    <tspan x="803" y="140">Courage</tspan>
    <tspan x="803" y="171">Accountability</tspan>
    <tspan x="803" y="202">Humility</tspan>
    <tspan x="803" y="233">Decisive</tspan>
    <tspan x="803" y="264">Curious</tspan>
    <tspan x="803" y="295">Integrity</tspan>
    <tspan x="803" y="326">Caring</tspan>
  </text>

  <!-- CAPITALISM -->
  <text class="value" x="869" y="436" font-size="96" textLength="537" lengthAdjust="spacingAndGlyphs">CAPITALISM</text>
  <text class="attributes">
    <tspan x="875" y="478">Honorable Cunning Competitive</tspan>
    <tspan x="875" y="509">Compartmentalization Conscientiousness</tspan>
    <tspan x="875" y="540">Innovative Perseverance</tspan>
  </text>

  <!-- headline -->
  <text class="headline" x="154" y="669" font-size="338" textLength="493" lengthAdjust="spacingAndGlyphs">CORE</text>
  <text class="headline" x="686" y="822" font-size="332" textLength="727" lengthAdjust="spacingAndGlyphs">VALUES</text>

  <!-- INDEPENDENCE -->
  <text class="value" font-size="92" textLength="707" lengthAdjust="spacingAndGlyphs" transform="translate(1521 1106) rotate(-90)">INDEPENDENCE</text>

  <!-- TRUST -->
  <text class="value" x="182" y="792" font-size="94" textLength="299" lengthAdjust="spacingAndGlyphs">TRUST</text>
  <text class="attributes">
    <tspan x="198" y="845">Humility Consistency</tspan>
    <tspan x="198" y="876">Open mindedness</tspan>
    <tspan x="198" y="907">Curiosity Selflessness</tspan>
    <tspan x="198" y="938">Caring Conscienti</tspan>
    <tspan x="198" y="969">ousness</tspan>
  </text>
  <rect class="block-teal" x="185" y="1004" width="203" height="92"/>
  <rect class="block-teal" x="406" y="1006" width="9" height="93"/>
  <rect class="block-teal" x="428" y="1006" width="9" height="93"/>
  <rect class="block-teal" x="449" y="1006" width="9" height="93"/>

  <!-- GROWTH -->
  <text class="value" font-size="92" textLength="402" lengthAdjust="spacingAndGlyphs" transform="translate(639 1131) rotate(-90)">GROWTH</text>
  <text class="attributes">
    <tspan x="665" y="873">Honorable</tspan>
    <tspan x="665" y="904">Cunning</tspan>
    <tspan x="665" y="935">Competitive</tspan>
    <tspan x="665" y="966">Compart</tspan>
    <tspan x="665" y="997">mentalization</tspan>
    <tspan x="665" y="1028">Conscien</tspan>
    <tspan x="665" y="1059">tiousness</tspan>
    <tspan x="665" y="1090">Innovative</tspan>
    <tspan x="665" y="1121">Perseverance</tspan>
  </text>

  <!-- lower right group -->
  <rect class="rule-navy" x="913" y="903" width="492" height="6"/>
  <text class="attributes attributes-right">
    <tspan x="1405" y="974">Humility Consistency Open</tspan>
    <tspan x="1405" y="1005">mindedness Curiosity</tspan>
    <tspan x="1405" y="1036">Selflessness Caring</tspan>
    <tspan x="1405" y="1067">Conscientiousness</tspan>
  </text>
  <rect class="rule-teal" x="893" y="1103" width="110" height="3"/>
  <rect class="rule-teal" x="1018" y="1103" width="110" height="3"/>
  <rect class="rule-teal" x="1138" y="1103" width="267" height="3"/>

  <!-- footer band -->
  <rect class="footer-band" x="0" y="1264" width="1686" height="36"/>
</svg>
</body>
</html>
```